Authenticity Diagnostic (How Authentic Are You in the Workplace?)

We run a consultancy business that supports organisations in changing the way they operate, in helping leaders and managers in to do their job and in supporting cultural change. We write various books on the topic with one coming out shortly called "Building Genuine Workplaces" by Colin Maxter and Nora Vellacott

We need to have a designed diagnostic tool (In 2 parts) that allows people to complete a 30 question self-diagnostic, that then tells them how authentic they are in the workplace, and in which aspects they are particularly strong/need help. We already have one that we have designed ourselves but need something that is a little more professional looking. However, the content and main presentation elements (such as the scoring process and graphs for completing scores) need to remain the same. We would also like to retain the main logo theme of the coloured fingerprint.

The audience for the tool will be employees within organisations of all sizes and sectors. It needs to be easy to follow, to carry some of the identifiers/images shown in the attached document (e.g the fingerprint, and the magenta colour), and as it relates to the workplace the styling shouldn't be too fancy.

Target Market(s)

Workers in ORGANISATIONS interested in how engaging their workplace is. Good for managers and team leaders

Industry/Entity Type

Business

Font styles to use
Sans Serif

Requirements
Must have
• Fingerprint image. Colours that work well with image. Consistent and clear use of shading (or better solution) to assist with scoring the diagnostic/ questionnaire. PLEASE BE AWARE we are not just (even) looking for a logo, we want a design, based on the original, of a questionnaire/answer booklet and the guidance notes that follow.
Should not have
• Not just a logo or cover design.

```html
<!DOCTYPE html>
<html lang="en">
<head>
<meta charset="utf-8">
<title>Authenticity Diagnostic – Questionnaire</title>
<link href="https://fonts.googleapis.com/css2?family=Roboto+Condensed:wght@400;700&display=swap" rel="stylesheet">
<style>
  :root {
    --magenta: #ec2f73;
    --row-white: #ffffff;
    --row-pale: #fbe0ea;
    --row-deep: #f8c9d9;
    --row-rule: #f3d3de;
    --ink: #231f20;
    --box-border: #ec2f73;
    --box-number: #7a7a7a;
  }
  * { box-sizing: border-box; margin: 0; padding: 0; }
  html, body { width: 848px; height: 1200px; overflow: hidden; background: #fff; }
  body { font-family: "Roboto Condensed", "Arial Narrow", sans-serif; color: var(--ink); }

  .sheet-header {
    height: 68px;
    background: var(--magenta);
    color: #fff;
    position: relative;
    padding: 8px 16px 0 24px;
  }
  .sheet-title { font-size: 29px; font-weight: 700; letter-spacing: 0.3px; line-height: 1.05; }
  .sheet-instruction { font-size: 15px; margin-top: 3px; }
  .scale-label {
    position: absolute; top: 22px; font-size: 13px; font-weight: 700; text-align: center; line-height: 1.1;
  }
  .scale-label span { display: block; font-size: 9px; }
  .scale-label--low { left: 636px; }
  .scale-label--high { left: 755px; }

  .question-list { list-style: none; }
  .question {
    height: 54.5px;
    display: flex;
    align-items: center;
    position: relative;
    border-bottom: 1px solid var(--row-rule);
  }
  .question:nth-child(3n+1) { background: var(--row-white); }
  .question:nth-child(3n+2) { background: var(--row-pale); }
  .question:nth-child(3n) { background: var(--row-deep); }
  .question-number { width: 40px; padding-left: 14px; font-size: 15px; }
  .question-text { width: 580px; font-size: 15px; line-height: 1.2; }
  .answer-scale { position: absolute; left: 643px; display: flex; gap: 8.5px; }
  .answer-box {
    width: 30px; height: 31px;
    border: 1.5px solid var(--box-border);
    border-radius: 5px;
    background: #fff;
    display: flex; align-items: center; justify-content: center;
    font-size: 15px; color: var(--box-number);
  }
</style>
</head>
<body>
  <header class="sheet-header">
    <h1 class="sheet-title">At work, to what extent do I feel able to…</h1>
    <p class="sheet-instruction">(Circle the corresponding number on the right for each question)</p>
    <div class="scale-label scale-label--low">Not at all<span>▼</span></div>
    <div class="scale-label scale-label--high">To a large extent<span>▼</span></div>
  </header>

  <ol class="question-list">
    <li class="question"><span class="question-number">1</span><span class="question-text">Organise my working day and manage my time as I judge appropriate to the job</span><div class="answer-scale"><span class="answer-box">0</span><span class="answer-box">1</span><span class="answer-box">2</span><span class="answer-box">3</span><span class="answer-box">4</span></div></li>
    <li class="question"><span class="question-number">2</span><span class="question-text">Raise concerns/highlight potential risks to the organisation, particularly<br>those risks that some may not wish to hear e.g. "the elephant in the room"</span><div class="answer-scale"><span class="answer-box">0</span><span class="answer-box">1</span><span class="answer-box">2</span><span class="answer-box">3</span><span class="answer-box">4</span></div></li>
    <li class="question"><span class="question-number">3</span><span class="question-text">Discuss the opportunities and scope for me to be authentic at work<br>(to be true to myself)</span><div class="answer-scale"><span class="answer-box">0</span><span class="answer-box">1</span><span class="answer-box">2</span><span class="answer-box">3</span><span class="answer-box">4</span></div></li>
    <li class="question"><span class="question-number">4</span><span class="question-text">Have discretion to take everyday decisions without involving more senior<br>members of staff (within reasonable limitations)</span><div class="answer-scale"><span class="answer-box">0</span><span class="answer-box">1</span><span class="answer-box">2</span><span class="answer-box">3</span><span class="answer-box">4</span></div></li>
    <li class="question"><span class="question-number">5</span><span class="question-text">Talk about my feelings and how they relate to my work (including being<br>able to show vulnerability)</span><div class="answer-scale"><span class="answer-box">0</span><span class="answer-box">1</span><span class="answer-box">2</span><span class="answer-box">3</span><span class="answer-box">4</span></div></li>
    <li class="question"><span class="question-number">6</span><span class="question-text">Arrange my physical workspace in a way that reflects who I am and the<br>way I like to work</span><div class="answer-scale"><span class="answer-box">0</span><span class="answer-box">1</span><span class="answer-box">2</span><span class="answer-box">3</span><span class="answer-box">4</span></div></li>
    <li class="question"><span class="question-number">7</span><span class="question-text">Discuss the opportunities and scope for me to be authentic at work<br>(to be true to myself)</span><div class="answer-scale"><span class="answer-box">0</span><span class="answer-box">1</span><span class="answer-box">2</span><span class="answer-box">3</span><span class="answer-box">4</span></div></li>
    <li class="question"><span class="question-number">8</span><span class="question-text">Have discretion to take everyday decisions without involving more senior<br>members of staff (within reasonable limitations)</span><div class="answer-scale"><span class="answer-box">0</span><span class="answer-box">1</span><span class="answer-box">2</span><span class="answer-box">3</span><span class="answer-box">4</span></div></li>
    <li class="question"><span class="question-number">9</span><span class="question-text">Talk about my feelings and how they relate to my work (including being<br>able to show vulnerability)</span><div class="answer-scale"><span class="answer-box">0</span><span class="answer-box">1</span><span class="answer-box">2</span><span class="answer-box">3</span><span class="answer-box">4</span></div></li>
    <li class="question"><span class="question-number">10</span><span class="question-text">Raise concerns/highlight potential risks to the organisation, particularly<br>those risks that some may not wish to hear e.g. "the elephant in the room"</span><div class="answer-scale"><span class="answer-box">0</span><span class="answer-box">1</span><span class="answer-box">2</span><span class="answer-box">3</span><span class="answer-box">4</span></div></li>
    <li class="question"><span class="question-number">11</span><span class="question-text">Discuss the opportunities and scope for me to be authentic at work<br>(to be true to myself)</span><div class="answer-scale"><span class="answer-box">0</span><span class="answer-box">1</span><span class="answer-box">2</span><span class="answer-box">3</span><span class="answer-box">4</span></div></li>
    <li class="question"><span class="question-number">12</span><span class="question-text">Have discretion to take everyday decisions without involving more senior<br>members of staff (within reasonable limitations)</span><div class="answer-scale"><span class="answer-box">0</span><span class="answer-box">1</span><span class="answer-box">2</span><span class="answer-box">3</span><span class="answer-box">4</span></div></li>
    <li class="question"><span class="question-number">13</span><span class="question-text">Talk about my feelings and how they relate to my work (including being<br>able to show vulnerability)</span><div class="answer-scale"><span class="answer-box">0</span><span class="answer-box">1</span><span class="answer-box">2</span><span class="answer-box">3</span><span class="answer-box">4</span></div></li>
    <li class="question"><span class="question-number">14</span><span class="question-text">Raise concerns/highlight potential risks to the organisation, particularly<br>those risks that some may not wish to hear e.g. "the elephant in the room"</span><div class="answer-scale"><span class="answer-box">0</span><span class="answer-box">1</span><span class="answer-box">2</span><span class="answer-box">3</span><span class="answer-box">4</span></div></li>
    <li class="question"><span class="question-number">15</span><span class="question-text">Discuss the opportunities and scope for me to be authentic at work<br>(to be true to myself)</span><div class="answer-scale"><span class="answer-box">0</span><span class="answer-box">1</span><span class="answer-box">2</span><span class="answer-box">3</span><span class="answer-box">4</span></div></li>
    <li class="question"><span class="question-number">16</span><span class="question-text">Have discretion to take everyday decisions without involving more senior<br>members of staff (within reasonable limitations)</span><div class="answer-scale"><span class="answer-box">0</span><span class="answer-box">1</span><span class="answer-box">2</span><span class="answer-box">3</span><span class="answer-box">4</span></div></li>
    <li class="question"><span class="question-number">17</span><span class="question-text">Talk about my feelings and how they relate to my work (including being<br>able to show vulnerability)</span><div class="answer-scale"><span class="answer-box">0</span><span class="answer-box">1</span><span class="answer-box">2</span><span class="answer-box">3</span><span class="answer-box">4</span></div></li>
    <li class="question"><span class="question-number">18</span><span class="question-text">Raise concerns/highlight potential risks to the organisation, particularly<br>those risks that some may not wish to hear e.g. "the elephant in the room"</span><div class="answer-scale"><span class="answer-box">0</span><span class="answer-box">1</span><span class="answer-box">2</span><span class="answer-box">3</span><span class="answer-box">4</span></div></li>
    <li class="question"><span class="question-number">19</span><span class="question-text">Discuss the opportunities and scope for me to be authentic at work<br>(to be true to myself)</span><div class="answer-scale"><span class="answer-box">0</span><span class="answer-box">1</span><span class="answer-box">2</span><span class="answer-box">3</span><span class="answer-box">4</span></div></li>
    <li class="question"><span class="question-number">20</span><span class="question-text">Have discretion to take everyday decisions without involving more senior<br>members of staff (within reasonable limitations)</span><div class="answer-scale"><span class="answer-box">0</span><span class="answer-box">1</span><span class="answer-box">2</span><span class="answer-box">3</span><span class="answer-box">4</span></div></li>
  </ol>
</body>
</html>
```